Fresh Harbor Laundromat

"Your Laundry Done Brightly! "
Free Pick up and delivery Laundry service.
Wash, dry, fold.
Commercial and Residential
Featuring Vela Purex Ozone sanitization
freshharborlaundromat-example.com
555-214-3087
Studio flock did our logo

K420 Arlo Voyager Medium Roof

Working professionals

laundry pick up and delivery

• Washing machine with logo

```html
<!DOCTYPE html>
<html lang="en">
<head>
<meta charset="utf-8">
<title>Fresh Harbor Laundromat – Free Pick Up and Delivery</title>
<link rel="stylesheet" href="https://fonts.googleapis.com/css2?family=Exo+2:wght@500;600&family=Lilita+One&family=Cormorant+SC:wght@500&display=swap">
<style>
  :root {
    --ink: #2f3d55;
    --ink-deep: #3a4660;
    --green: #6cc04a;
    --green-band: #4caf3f;
    --blue-band: #1f6a98;
    --bubble-a: #2f6f98;
    --bubble-b: #86acc2;
    --brand-blue: #1f5f8b;
    --white: #ffffff;
  }
  * { margin: 0; padding: 0; box-sizing: border-box; }
  html, body { width: 1200px; height: 439px; overflow: hidden; background: var(--white); }
  .banner { position: relative; width: 1200px; height: 439px; overflow: hidden; font-family: "Exo 2", sans-serif; color: var(--ink); }
  .banner-art { position: absolute; inset: 0; }

  .tagline {
    position: absolute; left: 523px; top: 78px; width: 200px;
    font-family: "Lilita One", sans-serif; font-size: 28px; line-height: 33px;
    color: var(--white); text-align: center; transform: rotate(7deg);
    letter-spacing: 0.5px;
  }

  .offer {
    position: absolute; left: 757px; top: 62px; width: 400px; text-align: center;
    transform: rotate(-1.5deg);
  }
  .offer-lines { font-weight: 600; font-size: 20.5px; line-height: 22px; color: var(--green); }
  .contact { margin-top: 8px; font-weight: 500; font-size: 14px; line-height: 19px; color: var(--ink); }
  .contact-item { display: inline-flex; align-items: center; gap: 5px; }
  .contact-item svg { width: 15px; height: 15px; }

  .step-label {
    position: absolute; top: 222px; width: 160px; text-align: center;
    font-weight: 500; font-size: 17.5px; color: var(--ink);
  }

  .brand { position: absolute; left: 252px; top: 282px; width: 170px; text-align: center; }
  .brand-name { font-weight: 600; font-size: 17px; line-height: 19px; color: var(--brand-blue); }
  .brand-mark { display: block; width: 18px; height: 18px; margin: 0 auto 6px; background: var(--brand-blue); }
  .brand-soon { font-family: "Cormorant SC", serif; font-size: 13px; color: var(--green-band); margin-top: 4px; }
  .brand-url { font-family: "Cormorant SC", serif; font-size: 5.5px; color: var(--brand-blue); }
</style>
</head>
<body>
<main class="banner">
  <svg class="banner-art" width="1200" height="439" viewBox="0 0 1200 439" aria-hidden="false">
    <defs>
      <linearGradient id="bubble-fill" x1="0" y1="0" x2="1" y2="0">
        <stop offset="0" stop-color="var(--bubble-a)"/>
        <stop offset="1" stop-color="var(--bubble-b)"/>
      </linearGradient>
    </defs>

    <!-- speech bubble -->
    <g class="speech-bubble">
      <path fill="var(--ink-deep)" d="M500,70 C540,30 650,25 710,45 C760,60 780,110 770,150 C760,190 710,200 660,195 C640,205 610,225 590,214 C600,202 596,196 580,196 C520,200 475,182 470,142 C466,110 480,85 500,70 Z"/>
      <path fill="url(#bubble-fill)" d="M508,70 C545,40 650,38 705,55 C748,68 762,110 752,146 C743,178 705,186 658,182 C635,190 618,205 605,200 C612,190 602,184 585,184 C530,186 490,170 487,136 C485,110 493,84 508,70 Z"/>
      <path fill="none" stroke="var(--ink-deep)" stroke-width="5" stroke-linecap="round" d="M503,58 Q522,40 552,32"/>
      <path fill="none" stroke="var(--ink-deep)" stroke-width="5" stroke-linecap="round" d="M729,57 Q776,95 770,150"/>
    </g>

    <!-- process steps -->
    <g class="step">
      <circle cx="561" cy="301" r="51" fill="var(--ink-deep)"/>
      <circle cx="561" cy="301" r="36" fill="#cfe3ee" role="img" aria-label="Wall clock illustration"/>
    </g>
    <g class="step">
      <circle cx="725" cy="297" r="51" fill="var(--ink-deep)"/>
      <ellipse cx="725" cy="297" rx="42" ry="28" fill="#7dc55a" role="img" aria-label="Laundry basket full of green clothes illustration"/>
    </g>
    <g class="step">
      <circle cx="886" cy="295" r="51" fill="var(--ink-deep)"/>
      <rect x="849" y="268" width="74" height="52" rx="8" fill="#74c257" role="img" aria-label="Stack of freshly folded clothes illustration"/>
    </g>
    <g class="step">
      <circle cx="1058" cy="292" r="51" fill="var(--ink-deep)"/>
      <rect x="1015" y="270" width="86" height="42" rx="8" fill="#e7efe9" role="img" aria-label="Delivery van illustration"/>
    </g>

    <!-- arrows between steps -->
    <g class="step-arrow" fill="var(--ink-deep)">
      <path d="M619,287 H645 V275 L666,297 L645,319 V307 H619 Z"/>
      <path d="M782,285 H808 V273 L829,295 L808,317 V305 H782 Z"/>
      <path d="M948,283 H974 V271 L995,293 L974,315 V303 H948 Z"/>
    </g>

    <!-- bottom bands -->
    <path class="band-blue" fill="var(--blue-band)" d="M0,418 L1200,405 L1200,439 L0,439 Z"/>
    <path class="band-green" fill="var(--green-band)" d="M0,430 L1200,419 L1200,439 L0,439 Z"/>
  </svg>

  <div class="tagline">Your Laundry<br>Done Brightly!</div>

  <section class="offer">
    <p class="offer-lines">Free Pick up and delivery<br>Laundry service<br>Commercial and Residential<br>Feat. Vela Purex Ozone sanitization</p>
    <div class="contact">
      <div class="contact-item">
        <svg viewBox="0 0 24 24" aria-hidden="true"><path fill="var(--ink)" d="M3,9 C3,5 21,5 21,9 L17,10 L16,8 H8 L7,10 Z M6,12 H18 L20,20 H4 Z"/><circle cx="12" cy="15.5" r="2.3" fill="#fff"/></svg>
        <span>555-214-3087</span>
      </div><br>
      <div class="contact-item">
        <svg viewBox="0 0 24 24" aria-hidden="true" fill="none" stroke="var(--ink)" stroke-width="1.6"><circle cx="12" cy="12" r="9.5"/><ellipse cx="12" cy="12" rx="4.2" ry="9.5"/><path d="M2.5,12 H21.5 M4,7 H20 M4,17 H20"/></svg>
        <span>freshharborlaundromat-example.com</span>
      </div>
    </div>
  </section>

  <div class="step-label" style="left:481px">Schedule it</div>
  <div class="step-label" style="left:641px; top:219px">Pick it up</div>
  <div class="step-label" style="left:803px; top:216px">Wash, dry, and fold</div>
  <div class="step-label" style="left:972px; top:213px">Drop it off</div>

  <div class="brand">
    <span class="brand-mark"></span>
    <p class="brand-name">Fresh Harbor<br>Laundromat</p>
    <p class="brand-soon">Coming Soon!</p>
    <p class="brand-url">freshharborlaundromat-example.com</p>
  </div>
</main>
</body>
</html>
```